Business Card for a Wellness and Aesthetic Center

I'd like to have a business card design for a Wellness and Aesthetic Center based in the Philippines called "Silvermoss Wellness and Aesthetic Inc." They provide services such as medical and aesthetic dermatology. Specializing on cosmetic and anti-aging procedures.

The target market of the business is mostly women from the upper class from 30 to 60 years old.

The feel and look of the card should be feminine, modern, minimalist and classy.

The colors to play with are gold and black.

The front part should contain:
- Name (example: Marisol Teravid Pangilan, MD)
- Designation (example: Medical Director)
- Company Logo

The back part should contain:
- Company Logo
- Address
- Contact Details
- Website

For more details and inspiration you may visit their website at http://silvermossph.com/

Thank you very much!

Target Market(s)

Women from the upper class from 30 to 60 years old.

Industry/Entity Type

Business

Contact Information for Business Card

- Company Logo

- Company Logo
- Address
- Contact Details
- Website

Font styles to use
Serif
Script

Colors
ffc214
fece3e
faa54b
f78f20
000000

Requirements
Must have
• Design should be feminine, modern, minimalist/simple and classy.
Nice to have
• You can play with lines, curves, gardient and be creative on the placement of texts and logo.
Should not have
• Pictures like body, face or nature scene.

```html
<!DOCTYPE html>
<html lang="en">
<head>
<meta charset="utf-8">
<title>Silvermoss Wellness and Aesthetic Inc. — Business Card</title>
<link rel="stylesheet" href="https://fonts.googleapis.com/css2?family=Arimo:wght@400&display=swap">
<style>
  :root {
    --ink: #000000;
    --gold: #e6900f;
    --gold-deep: #d98a0c;
    --paper: #ffffff;
    --name-white: #ffffff;
  }
  * { margin: 0; padding: 0; box-sizing: border-box; }
  html, body {
    width: 1200px;
    height: 313px;
    overflow: hidden;
    background: var(--paper);
    font-family: "Arimo", Arial, sans-serif;
  }
  .sheet {
    position: relative;
    width: 1200px;
    height: 313px;
  }
  .card {
    position: absolute;
    top: 0;
    height: 313px;
    background: var(--ink);
    overflow: hidden;
  }
  .card--back { left: 0; width: 565px; }
  .card--front { left: 633px; width: 567px; }

  .card__shape {
    position: absolute;
    inset: 0;
    width: 100%;
    height: 100%;
  }
  .card__shape path { fill: var(--gold); }

  .brand {
    position: absolute;
    color: var(--gold);
    font-size: 30px;
    font-weight: 400;
    letter-spacing: 0.5px;
    white-space: nowrap;
  }
  .card--back .brand { left: 24px; top: 100px; }
  .card--front .brand { left: 28px; top: 92px; }

  .address {
    position: absolute;
    left: 228px;
    top: 178px;
    width: 306px;
    text-align: center;
    color: var(--gold);
    font-size: 15.5px;
    line-height: 17px;
  }
  .address__phone {
    display: block;
    margin-top: 6px;
    font-size: 7px;
    line-height: 8px;
    text-decoration: underline;
  }
  .website {
    position: absolute;
    left: 58px;
    top: 283px;
    color: var(--gold);
    font-size: 11px;
    text-decoration: underline;
  }

  .holder {
    position: absolute;
    left: 300px;
    top: 247px;
    width: 256px;
    text-align: center;
    color: var(--name-white);
  }
  .holder__name {
    display: block;
    font-size: 18px;
    line-height: 20px;
  }
  .holder__title {
    display: block;
    margin-top: 2px;
    font-size: 12.5px;
    line-height: 14px;
  }
</style>
</head>
<body>
  <main class="sheet">
    <section class="card card--back" aria-label="Card back">
      <svg class="card__shape" viewBox="0 0 565 313" aria-hidden="true">
        <path d="M565 218 C558 268 525 300 478 313 L565 313 Z"/>
      </svg>
      <div class="brand">Silvermoss</div>
      <p class="address">
        Basement, North Crest Tower Sandoval<br>
        Business Park Alabang<br>
        Muntinlupa City
        <span class="address__phone">Ph.&nbsp; (632) 555-0148</span>
      </p>
      <span class="website">www.silvermossph.com</span>
    </section>

    <section class="card card--front" aria-label="Card front">
      <svg class="card__shape" viewBox="0 0 567 313" aria-hidden="true">
        <path d="M282 238 C302 214 362 212 430 215 C498 218 540 208 567 194 L567 313 L296 313 C266 300 262 262 282 238 Z"/>
      </svg>
      <div class="brand">Silvermoss</div>
      <p class="holder">
        <span class="holder__name">Marisol Teravid Pangilan</span>
        <span class="holder__title">(Medical Director)</span>
      </p>
    </section>
  </main>
</body>
</html>
```